Young and modern Electrical company working in the commercial arena.

Wanting a business card design thats modern and will last. Maybe Minimalist? Happy to look at changing my logo

Target Market(s)

Builders, Project Managers

Industry/Entity Type

Electrical

Contact Information for Business Card

Name
Address
Phone number
Job title

Logo Text

our name or just the logo i'm open to ideas

Font styles to use
Sans Serif

Requirements
Nice to have
• would like to keep the purple in our current logo. it's kinda unique to our market
Should not have
• Don't want it to be to busy. simple is best i think

```html
<!DOCTYPE html>
<html lang="en">
<head>
<meta charset="UTF-8">
<title>Halvorsen Electrical – Business Card</title>
<link href="https://fonts.googleapis.com/css2?family=Montserrat:wght@400;600;700;800&display=swap" rel="stylesheet">
<style>
  :root {
    --page-bg: #e9e6e1;
    --card-bg: #16151b;
    --card-edge: #24232b;
    --grid-line: rgba(255,255,255,0.035);
    --brand-purple: #7d62d3;
    --accent-orange: #f0871f;
    --text-light: #eceaf2;
    --text-muted: #c9c6d4;
    --emblem-faint: rgba(255,255,255,0.045);
  }
  * { box-sizing: border-box; margin: 0; padding: 0; }
  html, body { width: 900px; height: 1200px; overflow: hidden; }
  body {
    background: var(--page-bg);
    font-family: 'Montserrat', Arial, sans-serif;
    position: relative;
  }
  .card {
    position: absolute;
    left: 68px;
    width: 764px;
    height: 420px;
    border-radius: 20px;
    background-color: var(--card-bg);
    background-image:
      repeating-linear-gradient(0deg, var(--grid-line) 0 1px, transparent 1px 9px),
      repeating-linear-gradient(90deg, var(--grid-line) 0 1px, transparent 1px 9px);
    border: 1px solid var(--card-edge);
    box-shadow: 0 10px 28px rgba(0,0,0,0.35);
    overflow: hidden;
    color: var(--text-light);
  }
  .card--front { top: 160px; }
  .card--back { top: 640px; }

  .emblem-faint {
    position: absolute;
    width: 300px;
    height: 300px;
    border-radius: 50%;
    border: 22px solid var(--emblem-faint);
  }
  .card--front .emblem-faint { right: -30px; top: 150px; }
  .card--back .emblem-faint { right: -50px; top: 60px; }

  .brand {
    position: absolute;
    display: flex;
    align-items: center;
    gap: 14px;
  }
  .brand__dot {
    width: 58px;
    height: 58px;
    border-radius: 50%;
    border: 4px solid var(--brand-purple);
    flex: none;
  }
  .brand__name {
    color: var(--brand-purple);
    font-weight: 800;
    font-size: 30px;
    line-height: 1;
    letter-spacing: 0.5px;
    text-transform: uppercase;
  }
  .brand__name span { display: block; font-size: 17px; letter-spacing: 6px; margin-top: 5px; }
  .card--front .brand { left: 40px; top: 36px; }
  .card--back .brand { left: 50%; top: 50%; transform: translate(-50%, -50%); }
  .card--back .brand__dot { width: 72px; height: 72px; }
  .card--back .brand__name { font-size: 36px; }
  .card--back .brand__name span { font-size: 20px; letter-spacing: 7px; }

  .holder {
    position: absolute;
    right: 44px;
    top: 48px;
    text-align: center;
  }
  .holder__name { font-weight: 700; font-size: 21px; letter-spacing: 1px; text-transform: uppercase; }
  .holder__title { color: var(--brand-purple); font-weight: 600; font-size: 11px; letter-spacing: 1.5px; text-transform: uppercase; margin-top: 4px; }

  .contact-list {
    position: absolute;
    left: 40px;
    top: 218px;
    list-style: none;
    font-size: 14px;
    color: var(--text-muted);
  }
  .contact-list li { display: flex; align-items: flex-start; gap: 12px; margin-bottom: 8px; line-height: 1.35; }
  .contact-list svg { width: 15px; height: 15px; flex: none; margin-top: 2px; fill: var(--accent-orange); }
  .contact-list .no-icon { padding-left: 27px; margin-top: -8px; }
</style>
</head>
<body>
  <section class="card card--front">
    <div class="emblem-faint" aria-hidden="true"></div>
    <div class="brand">
      <div class="brand__dot"></div>
      <div class="brand__name">Halvorsen<span>Electrical</span></div>
    </div>
    <div class="holder">
      <div class="holder__name">Owen Marsh</div>
      <div class="holder__title">Managing Director</div>
    </div>
    <ul class="contact-list">
      <li>
        <svg viewBox="0 0 24 24"><path d="M6.6 10.8a15.1 15.1 0 0 0 6.6 6.6l2.2-2.2a1 1 0 0 1 1-.25 11.4 11.4 0 0 0 3.6.57 1 1 0 0 1 1 1V20a1 1 0 0 1-1 1A17 17 0 0 1 3 4a1 1 0 0 1 1-1h3.5a1 1 0 0 1 1 1c0 1.25.2 2.45.57 3.57a1 1 0 0 1-.25 1z"/></svg>
        555.014.2270
      </li>
      <li>
        <svg viewBox="0 0 24 24"><path d="M2 5h20v14H2z" fill="none"/><path d="M3 5h18a1 1 0 0 1 1 1v12a1 1 0 0 1-1 1H3a1 1 0 0 1-1-1V6a1 1 0 0 1 1-1zm9 7.2L20 7H4z"/></svg>
        owen@halvorsenelectric.com
      </li>
      <li>
        <svg viewBox="0 0 24 24"><path d="M12 2a7 7 0 0 0-7 7c0 5.2 7 13 7 13s7-7.8 7-13a7 7 0 0 0-7-7zm0 9.5A2.5 2.5 0 1 1 12 6.5a2.5 2.5 0 0 1 0 5z"/></svg>
        PO Box 42, Millbrook, PA 10000
      </li>
      <li class="no-icon">Owen Marsh</li>
    </ul>
  </section>

  <section class="card card--back">
    <div class="emblem-faint" aria-hidden="true"></div>
    <div class="brand">
      <div class="brand__dot"></div>
      <div class="brand__name">Halvorsen<span>Electrical</span></div>
    </div>
  </section>
</body>
</html>
```